I want a business letter head designed, one that I can have printed but also one that I can use as an insert for proforma documentation that is printed in house.

Business name : RJ Penfold & Associates
Address: PO Box 738
Tewantin Qld 4587

Type of business: Accounting practice- accounting, taxation, audit, self managed superannuation,

Colour scheme: black and blue - previously designed a business card; however the blue that is one the cards is very washed out and I am not particularly happy with it.

Industry/Entity Type

Business

```html
<!DOCTYPE html>
<html lang="en">
<head>
<meta charset="utf-8">
<title>RJ Penfold &amp; Associates – Letterhead</title>
<link rel="stylesheet" href="https://fonts.googleapis.com/css2?family=Tinos&display=swap">
<style>
  :root {
    --paper: #ffffff;
    --ink: #1a1a1a;
    --muted: #a3a3a3;
    --accent-pale: #d4e8f5;
  }
  html, body {
    margin: 0;
    padding: 0;
    overflow: hidden;
    background: var(--paper);
  }
  .letterhead {
    position: relative;
    width: 927px;
    height: 1200px;
    overflow: hidden;
    background: var(--paper);
    font-family: "Tinos", "Times New Roman", serif;
    color: var(--ink);
  }
  .backdrop {
    position: absolute;
    inset: 0;
    width: 927px;
    height: 1200px;
  }
  .brand-name {
    position: absolute;
    left: 72px;
    top: 66px;
    margin: 0;
    font-size: 25px;
    font-weight: 400;
    line-height: 30px;
    letter-spacing: 0.5px;
    color: var(--ink);
  }
  .return-address {
    position: absolute;
    left: 230px;
    top: 64px;
    margin: 0;
    font-style: normal;
    font-size: 18px;
    line-height: 22px;
    color: var(--muted);
  }
  .letter {
    position: absolute;
    left: 174px;
    top: 240px;
    width: 600px;
    font-size: 16px;
    line-height: 20px;
  }
  .letter p,
  .letter address {
    margin: 0 0 20px;
    font-style: normal;
    white-space: nowrap;
  }
  .letter .closing { margin-bottom: 60px; }
</style>
</head>
<body>
<div class="letterhead">
  <svg class="backdrop" viewBox="0 0 927 1200" aria-hidden="true">
    <circle cx="830" cy="1010" r="430" fill="var(--accent-pale)"/>
  </svg>

  <h1 class="brand-name">RJ Penfold<br>&amp; Associates</h1>
  <address class="return-address">PO Box 738<br>Tewantin Qld 4587</address>

  <main class="letter">
    <address class="recipient">
      Lenii Grusx<br>
      Title<br>
      Company Name<br>
      4321 First Street<br>
      Anytown, State ZIP<br>
      Date 9/10/14
    </address>

    <p class="salutation">Dear Trenz,</p>

    <p>Lorem ipsum dolor sit amet, consectetur adipiscing elit, set eiusmod tempor incidunt<br>
    et labore et dolore magna aliquam. Ut enim ad minim veniam, quis nostrud exerc.<br>
    Irure dolor in reprehend incididunt ut labore et dolore magna aliqua. Ut enim ad<br>
    minim veniam, quis nostrud exercitation ullamco laboris nisi ut aliquip ex ea commo-<br>
    do consequat. Duis aute irure dolor in reprehenderit in voluptate velit esse molestaie<br>
    cillum. Tia non ob ea soluad incom dereud facilis est er expedit distinct. Nam liber<br>
    te conscient to factor tum poen legum odioque civiuda et tam. Neque pecun modut<br>
    est neque nonor et imper ned libidig met, consectetur adipiscing elit, sed ut labore et<br>
    dolore magna aliquam is nostrud exercitation ullam mmodo consequet. Duis aute in<br>
    voluptate velit esse cillum dolore eu fugiat nulla pariatur.</p>

    <p>At vver eos et accusam dignissum qui blandit est praesent. Trenz pruca beynocguon<br>
    doas nog apoply su trenz ucu hugh rasoluguon monugor or trenz ucugwo jag scannar.<br>
    Wa hava laasad trenzsa gwo producgs su IdfoBraid, yop quiel geg ba solaly raspon-<br>
    subla rof trenzur sala ent dusgrubuguon. Offoctivo immoriatoly, hawrgaxeeis phat<br>
    eit sakem eit vory gast te Plok peish ba useing phen roxas. Eslo idaffacgad gef trenz<br>
    beynocguon quiel ba trenz Spraadshaag ent trenz dreek wirc procassidt program.<br>
    Cak pwico vux bolug incluros all uf cak sirucor hawrgasi itoms alung gith cakiw nog<br>
    pwicos.</p>

    <p>Plloaso mako nuto uf cakso dodtos anr koop a cupy uf cak vux noaw yerw phuno.<br>
    Whag schengos, uf efed, quiel ba mada su otrenzr swipontgwook proudgs hus yag su<br>
    ba dagarmidad. Plasa maku noga wipont trenzsa schengos ent kaap zux copy wipont<br>
    trenz kipg naar mixent phona. Cak pwico siructiun ruos nust apoply tyu cak UCU<br>
    sisulutiun munityuw uw.</p>

    <p class="closing">Sincerely yours,</p>

    <p class="signatory">Urna Semper</p>
  </main>
</div>
</body>
</html>
```